Website for PeakStride Functional Training

We would like to launch a website for our boutique gym, PeakStride Functional Training. We'd like the website to have a lot of lime green which is one of our colors in our logo. The website will have a description of our workouts, membership, free trial class and location information.

Target Market(s)

Fitness enthusiasts, health conscious people, target ages 20-65, people looking to get fit and healthy, people looking to lose weight

Industry/Entity Type

Gym

Coding

Number of Pages Required

1 page

Font styles to use
Serif

Colors
9ccb3b
34a7d8

Requirements
Must have
• A lot of lime green to match our logo. Let the website be fun, eye catchy. Our phone number which is 614-287-9153 to be easily dialed directly from our website.
Nice to have
• We would like to include this verbiage:
• -The Most FUN 1 hour workout
• -Affordable personal training/group training
• -Individualized workout programs
• -FUN workouts delivering results
• -Turn ON fat burn-The Most FUN 1 hour workout
• -Turn ON fat burning "EPOC" after burn
• We want our website to be easily seen on smart phones, iPads, Androids
Should not have
• Font that is hard on the eyes

```html
<!DOCTYPE html>
<html lang="en">
<head>
<meta charset="utf-8">
<title>PeakStride Functional Training</title>
<link rel="stylesheet" href="https://fonts.googleapis.com/css2?family=Montserrat:wght@400;600;700&family=Open+Sans:ital,wght@0,400;0,600;0,700;1,400&display=swap">
<style>
:root{
  --lime:#9ccb3b;
  --blue:#34a7d8;
  --ink:#1d1d1d;
  --text:#555;
  --muted:#777;
  --line:#d6d6d6;
  --white:#fff;
  --dark:#141414;
}
*{box-sizing:border-box;margin:0;padding:0}
html,body{width:1200px;height:2899px;overflow:hidden}
body{position:relative;background:var(--white);font-family:"Open Sans",Arial,sans-serif;color:var(--text)}
.abs{position:absolute}
.heading{font-family:"Montserrat",Arial,sans-serif;color:var(--ink)}
.kicker{font-size:24px;font-weight:400}
.title{font-size:32px;font-weight:700}
.btn-outline{position:absolute;display:flex;align-items:center;justify-content:center;font-family:"Montserrat",Arial,sans-serif;font-weight:600;font-size:12px;letter-spacing:.5px;text-transform:uppercase}

/* hero */
.hero{left:0;top:0;width:1200px;height:531px;background:radial-gradient(ellipse at 55% 60%,#3a3a3a 0%,#1c1c1c 55%,#0c0c0c 100%)}
.brand{left:100px;top:30px;display:flex;align-items:center;gap:10px;font-family:"Montserrat",Arial,sans-serif;font-weight:700;font-size:30px;color:var(--lime)}
.brand-dot{width:22px;height:22px;border-radius:50%;background:var(--lime)}
.brand small{display:block;font-size:14px;font-weight:700;margin-top:-2px}
.nav{left:395px;top:44px;display:flex;gap:34px;font-family:"Montserrat",Arial,sans-serif;font-weight:600;font-size:15px;color:var(--white)}
.nav .active{color:var(--lime)}
.hero-title{left:0;width:1200px;top:198px;text-align:center;font-family:"Montserrat",Arial,sans-serif;font-weight:700;font-size:50px;color:var(--white);letter-spacing:.5px}
.hero-sub{left:0;width:1200px;top:266px;text-align:center;font-family:"Open Sans",Arial,sans-serif;font-weight:600;font-size:25px;color:var(--white)}
.hero-btn{left:485px;top:324px;width:230px;height:44px;border:2px solid var(--white);color:var(--white);font-size:15px}
.dots{left:556px;top:470px;display:flex;gap:6px}
.dots span{width:14px;height:14px;border-radius:50%;border:2px solid var(--white)}
.dots .on{background:var(--lime);border-color:var(--lime)}

/* welcome */
.welcome-body{left:100px;top:716px;width:530px;font-size:12px;line-height:22px}
.welcome-body p+p{margin-top:18px}
.read-more{left:100px;top:918px;width:145px;height:38px;border:2px solid var(--line);color:var(--lime)}
.photo{position:absolute;box-shadow:0 2px 6px rgba(0,0,0,.25)}

/* features */
.feature{top:1061px;height:332px;width:398px;text-align:center;color:var(--white)}
.feature.blue{background:var(--blue)}
.feature.lime{background:var(--lime)}
.feature svg{position:absolute;left:159px;top:26px}
.feature h3{position:absolute;left:0;width:100%;top:142px;font-family:"Montserrat",Arial,sans-serif;font-size:22px;font-weight:700}
.feature p{position:absolute;left:44px;width:310px;top:181px;font-size:12px;line-height:20px}
.feature .btn-outline{left:124px;width:150px;top:267px;height:38px;border:2px solid var(--white);border-radius:20px;color:var(--white);font-size:12px}

/* videos */
.checklist{left:640px;top:1563px;list-style:none;font-size:12px}
.checklist li{height:33px;display:flex;align-items:center;gap:14px}
.video-btn{left:205px;top:1797px;width:265px;height:38px;border:2px solid var(--line);color:var(--lime)}

/* testimonials */
.testimonials{left:0;top:1925px;width:1200px;height:417px;background:linear-gradient(90deg,#111 0%,#1b1b1b 45%,#4a4a4a 70%,#222 100%)}
.quote{left:115px;top:2093px;width:420px;font-style:italic;font-size:12px;line-height:24px;color:#ddd}
.quote-mark{font-family:Georgia,serif;font-size:46px;color:#888}
.avatar{left:98px;top:2198px;width:80px;height:80px;border-radius:50%;border:3px solid var(--white);background:linear-gradient(#c99b78,#7d5c44)}
.client-name{left:196px;top:2228px;font-family:"Montserrat",Arial,sans-serif;font-weight:700;font-size:14px;color:var(--blue)}

/* contact */
.label{font-family:"Montserrat",Arial,sans-serif;font-weight:600;font-size:16px;color:var(--ink)}
.field{position:absolute;border:1px solid var(--line);font-size:12px;color:var(--muted);padding:8px 10px}
.submit{left:627px;top:2750px;width:76px;height:30px;border-radius:15px;background:var(--lime);color:var(--white);font-size:12px}
.info-row{position:absolute;left:783px;display:flex;align-items:center;gap:18px;font-size:12px;line-height:22px;color:var(--text)}
.info-icon{width:34px;height:34px;border-radius:50%;border:1px solid var(--line);display:flex;align-items:center;justify-content:center;flex:none}
.info-row a{color:inherit;text-decoration:none}
.socials{left:783px;top:2751px;display:flex;gap:6px}
.socials span{width:28px;height:28px;border-radius:50%}
.footer-rule{left:98px;top:2820px;width:1004px;height:1px;background:var(--line)}
.copyright{left:0;width:1200px;top:2858px;text-align:center;font-size:12px;color:var(--muted)}
</style>
</head>
<body>

<!-- Hero -->
<section class="abs hero" role="img" aria-label="Two athletes lifting barbells in a dark gym"></section>
<div class="abs brand"><span class="brand-dot"></span><div>PeakStride<small>Functional Training</small></div></div>
<nav class="abs nav">
  <span class="active">Home</span><span>About us</span><span>Workouts</span><span>Membership</span><span>Free Trial Classes</span><span>Location</span>
  <svg width="16" height="16" viewBox="0 0 16 16" style="margin-top:2px"><circle cx="6.5" cy="6.5" r="5" fill="none" stroke="#fff" stroke-width="2.2"/><line x1="10" y1="10" x2="15" y2="15" stroke="#fff" stroke-width="2.6"/></svg>
</nav>
<h1 class="abs hero-title">PEAKSTRIDE FUNCTIONAL TRAINING</h1>
<p class="abs hero-sub">We are Affordable personal training/group training</p>
<div class="btn-outline hero-btn">Free Trial Classes</div>
<div class="abs dots"><span class="on"></span><span></span><span></span><span></span><span></span></div>

<!-- Welcome -->
<div class="abs heading kicker" style="left:100px;top:620px">Welcome to</div>
<h2 class="abs heading title" style="left:100px;top:652px">PeakStride Functional Training</h2>
<div class="abs welcome-body">
  <p>Our coaches build every session around real movement, steady progress and plenty of energy, so each hour feels short and every visit counts.</p>
  <p>Train in small groups or one on one with a coach who knows your goals. We track your lifts, adjust your plan and keep the pace fun. New members get a full assessment, a clear program and support from day one until results show.</p>
</div>
<div class="btn-outline read-more">Read more &gt;&gt;</div>
<div class="photo" role="img" aria-label="Woman training with dumbbells in a gym" style="left:780px;top:595px;width:322px;height:182px;background:linear-gradient(135deg,#1f2c3c,#3c4d60 60%,#1a2330)"></div>
<div class="photo" role="img" aria-label="Couple stretching together on grass outdoors" style="left:680px;top:777px;width:335px;height:210px;border:3px solid #fff;background:linear-gradient(180deg,#6f9a4a,#9ec46a 55%,#5d8a36)"></div>

<!-- Features -->
<div class="abs feature blue" style="left:0">
  <svg width="80" height="80" viewBox="0 0 80 80" fill="#fff"><circle cx="18" cy="22" r="9"/><path d="M8 48c0-8 8-12 14-8l12 10h26l10-16 6 4-12 22H34L20 50v14H8z"/><rect x="4" y="64" width="72" height="6" rx="3"/></svg>
  <h3>Workouts</h3>
  <p>Strength, cardio and mobility blended into fast, fun circuits that change every week to keep your body guessing.</p>
  <div class="btn-outline">Read more</div>
</div>
<div class="abs feature lime" style="left:401px">
  <svg width="80" height="80" viewBox="0 0 80 80"><rect x="6" y="10" width="56" height="54" rx="3" fill="#fff"/><rect x="16" y="4" width="6" height="12" fill="#fff"/><rect x="46" y="4" width="6" height="12" fill="#fff"/><g fill="#9ccb3b"><rect x="12" y="24" width="9" height="8"/><rect x="25" y="24" width="9" height="8"/><rect x="38" y="24" width="9" height="8"/><rect x="12" y="36" width="9" height="8"/><rect x="25" y="36" width="9" height="8"/><rect x="12" y="48" width="9" height="8"/></g><circle cx="58" cy="58" r="17" fill="#fff" stroke="#9ccb3b" stroke-width="3"/><path d="M58 48v10h8" stroke="#9ccb3b" stroke-width="3" fill="none"/></svg>
  <h3>Free Trial Classes</h3>
  <p>Pick any class on the calendar and try a full session free with a coach by your side.</p>
  <div class="btn-outline">View calendar</div>
</div>
<div class="abs feature blue" style="left:802px">
  <svg width="80" height="80" viewBox="0 0 80 80" fill="#fff"><circle cx="40" cy="22" r="12"/><circle cx="17" cy="28" r="9"/><circle cx="63" cy="28" r="9"/><path d="M20 70c0-16 8-26 20-26s20 10 20 26z"/><path d="M2 66c0-12 6-20 15-20 4 0 7 1 9 3-5 5-8 11-8 17z"/><path d="M78 66c0-12-6-20-15-20-4 0-7 1-9 3 5 5 8 11 8 17z"/></svg>
  <h3>Membership</h3>
  <p>Flexible plans for groups and private coaching, with no long contracts and friendly support.</p>
  <div class="btn-outline">Become a member</div>
</div>

<!-- Videos -->
<div class="photo" role="img" aria-label="Woman stretching on a gym floor, workout video preview" style="left:98px;top:1470px;width:477px;height:292px;background:linear-gradient(180deg,#b9b4ad,#8b857d 60%,#5e5953)"></div>
<svg class="abs" style="left:306px;top:1580px" width="60" height="60" viewBox="0 0 60 60"><circle cx="30" cy="30" r="29" fill="#2a2a2a" stroke="#fff" stroke-width="2"/><path d="M23 18l18 12-18 12z" fill="#fff"/></svg>
<div class="btn-outline video-btn">Search more workout videos</div>
<div class="abs heading kicker" style="left:640px;top:1462px">Workout videos for</div>
<h2 class="abs heading title" style="left:640px;top:1495px">Every Fitness level</h2>
<ul class="abs checklist">
  <li><svg width="14" height="14" viewBox="0 0 14 14"><circle cx="7" cy="7" r="7" fill="#9ccb3b"/><path d="M3.5 7.2l2.3 2.3 4.7-4.7" stroke="#fff" stroke-width="1.8" fill="none"/></svg>The Most FUN 1 hour workout</li>
  <li><svg width="14" height="14" viewBox="0 0 14 14"><circle cx="7" cy="7" r="7" fill="#9ccb3b"/><path d="M3.5 7.2l2.3 2.3 4.7-4.7" stroke="#fff" stroke-width="1.8" fill="none"/></svg>Affordable personal training/group training</li>
  <li><svg width="14" height="14" viewBox="0 0 14 14"><circle cx="7" cy="7" r="7" fill="#9ccb3b"/><path d="M3.5 7.2l2.3 2.3 4.7-4.7" stroke="#fff" stroke-width="1.8" fill="none"/></svg>ndividualized workout programs</li>
  <li><svg width="14" height="14" viewBox="0 0 14 14"><circle cx="7" cy="7" r="7" fill="#9ccb3b"/><path d="M3.5 7.2l2.3 2.3 4.7-4.7" stroke="#fff" stroke-width="1.8" fill="none"/></svg>FUN workouts delivering results</li>
  <li><svg width="14" height="14" viewBox="0 0 14 14"><circle cx="7" cy="7" r="7" fill="#9ccb3b"/><path d="M3.5 7.2l2.3 2.3 4.7-4.7" stroke="#fff" stroke-width="1.8" fill="none"/></svg>Turn ON fat burn-The Most FUN 1 hour workout</li>
  <li><svg width="14" height="14" viewBox="0 0 14 14"><circle cx="7" cy="7" r="7" fill="#9ccb3b"/><path d="M3.5 7.2l2.3 2.3 4.7-4.7" stroke="#fff" stroke-width="1.8" fill="none"/></svg>Affordable personal training/group training</li>
  <li><svg width="14" height="14" viewBox="0 0 14 14"><circle cx="7" cy="7" r="7" fill="#9ccb3b"/><path d="M3.5 7.2l2.3 2.3 4.7-4.7" stroke="#fff" stroke-width="1.8" fill="none"/></svg>Individualized workout programs</li>
  <li><svg width="14" height="14" viewBox="0 0 14 14"><circle cx="7" cy="7" r="7" fill="#9ccb3b"/><path d="M3.5 7.2l2.3 2.3 4.7-4.7" stroke="#fff" stroke-width="1.8" fill="none"/></svg>FUN workouts delivering results</li>
  <li><svg width="14" height="14" viewBox="0 0 14 14"><circle cx="7" cy="7" r="7" fill="#9ccb3b"/><path d="M3.5 7.2l2.3 2.3 4.7-4.7" stroke="#fff" stroke-width="1.8" fill="none"/></svg>Turn ON fat burning "EPOC" after burn</li>
</ul>

<!-- Testimonials -->
<section class="abs testimonials" role="img" aria-label="Athlete with chalked hands gripping a kettlebell"></section>
<div class="abs heading kicker" style="left:100px;top:1982px;color:#fff">Client</div>
<h2 class="abs heading title" style="left:100px;top:2014px;color:#fff">Testimonials</h2>
<span class="abs quote-mark" style="left:100px;top:2070px">&ldquo;</span>
<p class="abs quote">The coaches here made training fun again. I have more energy, I sleep better and I have never missed a session since I joined.</p>
<span class="abs quote-mark" style="left:505px;top:2150px">&rdquo;</span>
<div class="abs avatar" role="img" aria-label="Client portrait"></div>
<div class="abs client-name">MARCUS HALE</div>
<svg class="abs" style="left:502px;top:2230px" width="28" height="13" viewBox="0 0 28 13"><circle cx="6" cy="6.5" r="6" fill="#9ccb3b"/><path d="M7.5 4l-3 2.5 3 2.5" stroke="#222" stroke-width="1.5" fill="none"/><circle cx="22" cy="6.5" r="6" fill="#9ccb3b"/><path d="M20.5 4l3 2.5-3 2.5" stroke="#222" stroke-width="1.5" fill="none"/></svg>

<!-- Contact -->
<div class="abs heading kicker" style="left:0;width:1200px;text-align:center;top:2420px">Get in</div>
<h2 class="abs heading title" style="left:0;width:1200px;text-align:center;top:2452px">Touch with Us</h2>
<div class="abs label" style="left:98px;top:2538px">Contact Form:</div>
<div class="field" style="left:98px;top:2578px;width:297px;height:34px">Name :</div>
<div class="field" style="left:406px;top:2578px;width:297px;height:34px">Phone :</div>
<div class="field" style="left:98px;top:2622px;width:605px;height:34px">Email :</div>
<div class="field" style="left:98px;top:2666px;width:605px;height:72px">Message :</div>
<div class="btn-outline submit">Submit</div>

<div class="abs label" style="left:783px;top:2538px">Contact Information</div>
<div class="info-row" style="top:2580px">
  <span class="info-icon"><svg width="12" height="16" viewBox="0 0 12 16"><path d="M6 0a6 6 0 0 0-6 6c0 4.5 6 10 6 10s6-5.5 6-10a6 6 0 0 0-6-6z" fill="#34a7d8"/><circle cx="6" cy="6" r="2.2" fill="#fff"/></svg></span>
  <span>415 Birchline Avenue, Suite 12<br>Columbus, OH 43215</span>
</div>
<div class="info-row" style="top:2648px">
  <span class="info-icon"><svg width="14" height="14" viewBox="0 0 14 14"><path d="M3 1l2.5 3-1.5 1.6c.8 1.8 2.2 3.2 4 4L9.6 8.1 13 10.5 11.5 13C6 13 1 8 1 2.5z" fill="#34a7d8"/></svg></span>
  <a href="tel:+16142879153">614-287-9153</a>
</div>
<div class="info-row" style="top:2711px">
  <span class="info-icon"><svg width="14" height="11" viewBox="0 0 14 11"><rect width="14" height="11" rx="1.5" fill="#34a7d8"/><path d="M1 1.5l6 4.5 6-4.5" stroke="#fff" stroke-width="1.3" fill="none"/></svg></span>
  <span>info@peakstridetraining.com</span>
</div>
<div class="abs socials"><span style="background:#3b5998"></span><span style="background:#1da1f2"></span><span style="background:#d9352b"></span><span style="background:#a0795a"></span></div>

<div class="abs footer-rule"></div>
<p class="abs copyright">Copyrights &copy; 2017, PeakStride Functional Training . All Rights Reserved.</p>

</body>
</html>
```